The Larkwell Stillhouse - Gin Bottle Label

Hi Designers,

We are currently looking for some fresh ideas regarding a label for our gin bottle. We are relatively small and with an emphasis on a quality tipple
made from the very finest and responsibly sourced botanicals. Our operation concentrates on small batch/hand crafted in its purest sense and we would like to reflect this in our brand.
We are looking for a label to read The Larkwell Stillhouse and have feminine accents with a primary background colour similar to Marlowe green/blue. Things like Sakura branches with blossom, floral, pretty scrolling perhaps around either full or partial boarder. Gold foil might be used to accent the black border/highlight the word "The Larkwell Stillhouse" and perhaps any floral pattern.
There could reconsideration given to include two boxes "Batch No" and "Bottle No" which would remain empty and filled out by hand during bottling.
Our gin will be 45%ABV
Some floral designs might look good as though they were watercolours in appearance perhaps.
Our bottles are clear medicine style of which I shall attatch a pic.
We are pretty excited about this and would invite anyone with flair and great ideas to have fun with this design.

With kind regards,

Ned

Target Market(s)

People who adore bespoke Gin and would be predominately female.

Colors
86cfc6

Requirements
Must have
• We love the Marlowe green tones and this well may be our label colour with your design.
• The Larkwell Stillhouse - Gin - 45ABV
Nice to have
• Batch No & Bottle No boxes

```html
<!DOCTYPE html>
<html lang="en">
<head>
<meta charset="utf-8">
<title>The Larkwell Stillhouse – Gin Label</title>
<link rel="stylesheet" href="https://fonts.googleapis.com/css2?family=Cormorant+Garamond:wght@500;600;700&family=Sofia+Sans+Condensed:wght@600&display=swap">
<style>
  :root {
    --page: #f3f5f4;
    --label: #86cfc6;
    --label-light: #9fdcd3;
    --label-deep: #6cc2b6;
    --ink: #2a2f2e;
    --ink-soft: #3d4644;
    --teal-ink: #2f6b66;
    --dot: #ffffff;
    --pill-ink: #f1ead6;
    --scroll-tone: rgba(42, 58, 55, 0.22);
    --blossom-tone: rgba(240, 182, 204, 0.7);
    --corner-tone: rgba(255, 255, 255, 0.55);
  }
  * { margin: 0; padding: 0; box-sizing: border-box; }
  html, body { width: 1158px; height: 1200px; overflow: hidden; background: var(--page); }
  .label {
    position: absolute; left: 84px; top: 25px; width: 990px; height: 1150px;
    background: linear-gradient(180deg, var(--label-light) 0%, var(--label) 40%, var(--label-deep) 100%);
    box-shadow: 0 6px 24px rgba(0,0,0,0.12);
    font-family: "Cormorant Garamond", Georgia, serif;
    color: var(--ink);
  }
  .label > * { z-index: 1; }
  .dotted-frame {
    position: absolute; left: 40px; top: 34px; right: 40px; bottom: 34px;
    border: 5px dotted var(--dot);
  }
  .corner {
    position: absolute; width: 62px; height: 62px; border-radius: 8px;
    background: var(--corner-tone);
  }
  .corner--tl { left: 14px; top: 10px; }
  .corner--tr { right: 14px; top: 10px; }
  .corner--bl { left: 14px; bottom: 10px; }
  .corner--br { right: 14px; bottom: 10px; }
  .scrollwork {
    position: absolute; left: 130px; top: 20px; width: 730px; height: 180px;
    border-radius: 50%;
    background: radial-gradient(ellipse at 50% 50%, var(--scroll-tone) 0%, rgba(42,58,55,0.08) 55%, transparent 75%);
  }
  .brand {
    position: absolute; left: 60px; right: 60px; top: 222px;
    text-align: center; white-space: nowrap;
    font-weight: 700; font-size: 108px; line-height: 1.02;
    text-transform: uppercase; letter-spacing: 1px; color: var(--ink);
  }
  .tagline {
    position: absolute; left: 0; right: 0; top: 540px; text-align: center;
    font-family: "Sofia Sans Condensed", "Arial Narrow", sans-serif; font-weight: 600;
    font-size: 40px; letter-spacing: 8px; color: var(--teal-ink);
  }
  .batch-frame { position: absolute; left: 191px; top: 652px; width: 612px; height: 200px; }
  .abv {
    position: absolute; left: 384px; top: 652px; width: 222px; height: 58px; border-radius: 29px;
    background: var(--ink); color: var(--pill-ink);
    display: flex; align-items: center; justify-content: center;
    font-size: 40px; font-weight: 500;
  }
  .production {
    position: absolute; left: 0; right: 0; top: 724px; text-align: center;
    font-size: 48px; font-weight: 500; color: var(--ink);
  }
  .numbers {
    position: absolute; left: 0; right: 0; top: 818px;
    display: flex; justify-content: center; align-items: center; gap: 12px;
    font-size: 27px; color: var(--ink-soft);
  }
  .numbers__box { width: 62px; height: 32px; border-radius: 16px; background: #eef3f2; }
  .numbers__gap { width: 6px; }
  .divider { position: absolute; left: 284px; top: 890px; width: 430px; height: 20px; }
  .origin {
    position: absolute; left: 0; right: 0; top: 950px; text-align: center; color: var(--ink-soft);
  }
  .origin__country { font-size: 33px; line-height: 42px; font-weight: 500; }
  .origin__line { font-size: 28px; line-height: 40px; font-weight: 500; }
  .blossom {
    position: absolute; left: 46px; top: 620px; width: 108px; height: 480px;
    border-radius: 40% 60% 30% 50%;
    background: linear-gradient(160deg, var(--blossom-tone) 0%, rgba(226,160,186,0.4) 60%, rgba(120,90,80,0.15) 100%);
    z-index: 0;
  }
</style>
</head>
<body>
  <main class="label">
    <div class="dotted-frame"></div>
    <div class="corner corner--tl" role="img" aria-label="Ornamental corner flourish"></div>
    <div class="corner corner--tr" role="img" aria-label="Ornamental corner flourish"></div>
    <div class="corner corner--bl" role="img" aria-label="Ornamental corner flourish"></div>
    <div class="corner corner--br" role="img" aria-label="Ornamental corner flourish"></div>

    <div class="scrollwork" role="img" aria-label="Decorative scrolling vines and leaves crowning the label"></div>

    <div class="blossom" role="img" aria-label="Watercolour sakura branch with pink blossom rising along the left edge"></div>

    <h1 class="brand">The Larkwell<br>Stillhouse</h1>

    <p class="tagline">PREMIUM GIN</p>

    <svg class="batch-frame" viewBox="0 0 612 200" aria-hidden="true">
      <path d="M180 18 H22 Q10 18 10 30 V60" fill="none" stroke="#2a2f2e" stroke-width="6" stroke-linecap="round"/>
      <path d="M432 18 H590 Q602 18 602 30 V60" fill="none" stroke="#2a2f2e" stroke-width="6" stroke-linecap="round"/>
      <path d="M10 140 V162 Q10 174 22 174 H90" fill="none" stroke="#2a2f2e" stroke-width="6" stroke-linecap="round"/>
      <path d="M602 140 V162 Q602 174 590 174 H540" fill="none" stroke="#2a2f2e" stroke-width="6" stroke-linecap="round"/>
    </svg>
    <div class="abv">45%ABV</div>

    <p class="production">Premium Small Batch Production</p>

    <div class="numbers">
      <span>Batch No</span><span class="numbers__box"></span>
      <span class="numbers__gap"></span>
      <span>&amp; Bottle No</span><span class="numbers__box"></span>
    </div>

    <svg class="divider" viewBox="0 0 430 20" aria-hidden="true">
      <line x1="8" y1="10" x2="422" y2="10" stroke="#f4faf8" stroke-width="2.5"/>
      <circle cx="6" cy="10" r="4" fill="#f4faf8"/>
      <circle cx="424" cy="10" r="4" fill="#f4faf8"/>
      <path d="M215 2 L223 10 L215 18 L207 10 Z" fill="#f4faf8"/>
    </svg>

    <div class="origin">
      <p class="origin__country">Product of Country Name</p>
      <p class="origin__line">123 321 Street Name,</p>
      <p class="origin__line">Country 89175A</p>
    </div>
  </main>
</body>
</html>
```